Korellas Einfühlungsvermögen in das Projekt, ihre Nachfragen an der richtigen Stelle und ihre frischen Ideen haben zu einem ebook-Cover geführt, mit dem ich sehr zufrieden bin. Die Kommunikation war sehr angenehm und professionell. Danke!
Zielgruppe
E-Book: Satirische Kurzgeschichten rund um Schule und Bildung.
Zielgruppe: Leute mit Humor und Interesse an einem Einblick ins Klassenzimmer einer jungen Berliner Lehrerin. Schüler, Eltern, Lehrer, Referendare...
Aufgabenstellung
Möglichst keine Comics mit Sprechblasen, eher stilvoll, intellektuell, trotzdem frisch, jung und modern.
Helle Farben, gerne Andeutungen der Themen Schule, Bildung, Unterricht.
Die Kurzgeschichten meines E-Books sind schnelle Momentaufnahmen, sie könnten auch als Blog erscheinen statt als Buch, evtl. lässt sich dies auch im Design widerspiegeln (?).

```html
<!DOCTYPE html>
<html lang="de">
<head>
<meta charset="utf-8">
<title>Kreide und Kaffee – E-Book-Cover</title>
<link rel="stylesheet" href="https://fonts.googleapis.com/css2?family=Arimo&family=Cabin+Sketch:wght@700&family=Architects+Daughter&display=swap">
<style>
  :root {
    --page: #ffffff;
    --frame: #111111;
    --board-dark: #23564f;
    --board-mid: #2f6a63;
    --board-light: #4f8a84;
    --chalk: #eef1ef;
    --photo-warm: #b4603a;
    --photo-deep: #7e3a20;
    --photo-pale: #cfcac4;
  }
  html, body {
    margin: 0;
    padding: 0;
    width: 848px;
    height: 1200px;
    overflow: hidden;
    background: var(--page);
  }
  .page {
    position: relative;
    width: 848px;
    height: 1200px;
  }
  .cover {
    position: absolute;
    left: 137px;
    top: 176px;
    width: 602px;
    height: 850px;
    box-sizing: border-box;
    border: 1px solid var(--frame);
    overflow: hidden;
  }
  .cover__board {
    position: absolute;
    inset: 0;
    background:
      radial-gradient(ellipse at 78% 65%, var(--board-light) 0%, transparent 60%),
      linear-gradient(160deg, var(--board-dark) 0%, var(--board-mid) 55%, var(--board-dark) 100%);
  }
  .cover__photo {
    position: absolute;
    left: 0;
    top: 290px;
    width: 250px;
    height: 560px;
    background: linear-gradient(180deg, var(--photo-warm) 0%, var(--photo-deep) 50%, var(--photo-pale) 100%);
  }
  .cover__author {
    position: absolute;
    top: 32px;
    left: 0;
    right: 0;
    text-align: center;
    font-family: "Arimo", Arial, sans-serif;
    font-size: 28px;
    line-height: 34px;
    color: var(--chalk);
  }
  .cover__title {
    position: absolute;
    left: 0;
    right: 0;
    top: 78px;
    margin: 0;
    text-align: center;
    font-family: "Cabin Sketch", cursive;
    font-weight: 700;
    font-size: 86px;
    line-height: 100px;
    color: var(--chalk);
    text-transform: uppercase;
    letter-spacing: 2px;
  }
  .cover__subtitle {
    position: absolute;
    left: 266px;
    top: 318px;
    margin: 0;
    font-family: "Architects Daughter", cursive;
    font-size: 38px;
    line-height: 54px;
    color: var(--chalk);
    text-transform: uppercase;
    letter-spacing: 1px;
  }
</style>
</head>
<body>
  <div class="page">
    <section class="cover">
      <div class="cover__board" role="img" aria-label="Grüne Schultafel als Hintergrund"></div>
      <div class="cover__photo" role="img" aria-label="Foto einer jungen rothaarigen Lehrerin im karierten Hemd, die mit Kreide an die Tafel schreibt"></div>
      <div class="cover__author">HELGA PRINZ:</div>
      <h1 class="cover__title">Kreide und<br>Kaffee.</h1>
      <p class="cover__subtitle">Notizen vom<br>Lehrerpult</p>
    </section>
  </div>
</body>
</html>
```